KWT Contracting services . Building and maintenance services, optic fibre installation

Business cards and logo design.I need a logo that I can use on business cards ,workwear and on my vehicles. I would like the KWT to be the main or larger text and contracting services to be the smaller or less important text.I like monograms, modern designs and repeating patterns symbols. I am also a Gemini and my favourite number is 22 so if this can be any inspiration to help with the design. Am thinking of the using German flag colours as a his is my family’s heritage. And the other 2 main colours I wear is black and white.But any ideas are appreciated.I do not need a design that is trade specific but a design that could be used for any business.

Target Market(s)

General public

Contact Information for Business Card

KWT Contracting Services ( front of business card)

(Back of business card)
Milo Brackwood
0471539264
Maintenance services
Optic fibre and data installation

Logo Text

Logo can just be pattern or monogram or incorporate KWT . I like the gemini star sign and the number 22

Colors
ec1f27
000000
fbee3e
ffffff

Requirements
Must have
• Logo and KWT Contracting Services on the front of business card
Nice to have
• Possible use of German flag colours.
• Modern design.
• Design to be able to be used on black or white background as I want to put it on clothing

```html
<!DOCTYPE html>
<html lang="en">
<head>
<meta charset="utf-8">
<title>KWT Contracting Services – Business Cards</title>
<link rel="stylesheet" href="https://fonts.googleapis.com/css2?family=Jost:wght@500;600;800&display=swap">
<style>
  :root {
    --red: #ec1f27;
    --black: #000000;
    --board: #0b0b0c;
    --white: #ffffff;
    --ink: #231f20;
  }
  html, body {
    margin: 0;
    padding: 0;
    width: 1200px;
    height: 1200px;
    overflow: hidden;
    background: var(--white);
  }
  .canvas { display: block; width: 1200px; height: 1200px; }
  .board { fill: var(--board); }
  .card-black { fill: var(--black); }
  .card-white { fill: var(--white); }
  .accent { fill: var(--red); }
  .brand-name {
    font-family: "Jost", "Century Gothic", sans-serif;
    font-weight: 800;
    font-size: 118px;
    fill: var(--white);
    letter-spacing: -2px;
  }
  .brand-tagline {
    font-family: "Jost", "Century Gothic", sans-serif;
    font-weight: 600;
    font-size: 17px;
    letter-spacing: 5.2px;
    fill: var(--white);
  }
  .contact-line {
    font-family: "Jost", "Century Gothic", sans-serif;
    font-weight: 600;
    font-size: 22px;
    fill: var(--ink);
  }
</style>
</head>
<body>
<svg class="canvas" viewBox="0 0 1200 1200" xmlns="http://www.w3.org/2000/svg">
  <rect class="board" x="66" y="111" width="1027" height="1026"/>

  <!-- Card front -->
  <g class="card-front">
    <rect class="card-black" x="262" y="218" width="570" height="326"/>
    <rect class="accent" x="670" y="218" width="162" height="326"/>
    <path class="card-black" d="M670,292 L676,292 Q692,298 692,318 L692,448 Q692,468 676,474 L670,474 Z"/>
    <path class="accent" d="M262,288 Q288,296 288,322 L288,442 Q288,466 262,474 Z"/>
    <text class="brand-name" x="312" y="410">KWT</text>
    <text class="brand-tagline" x="314" y="440">CONTRACTING SERVICES</text>
  </g>

  <!-- Card back -->
  <g class="card-back">
    <rect class="card-white" x="260" y="707" width="571" height="325"/>
    <path class="accent" d="M428,707 L664,707 L664,725 Q664,743 646,743 L446,743 Q428,743 428,725 Z"/>
    <rect class="accent" x="260" y="945" width="571" height="87"/>
    <path class="card-white" d="M418,945 Q432,968 456,968 L634,968 Q658,968 672,945 Z"/>
    <text class="contact-line" x="350" y="811">MILO BRACKWOOD</text>
    <text class="contact-line" x="350" y="841">0471539264</text>
    <text class="contact-line" x="350" y="870">MAINTENANCE SERVICES</text>
    <text class="contact-line" x="350" y="900">OPTIC FIBRE AND DATA INSTALLATION</text>
  </g>
</svg>
</body>
</html>
```